Flyer Design für Kosmetikerin und Visagistin gesucht
Zielgruppe
Ich bin ein Einmannbetrieb und biete Kosmetik für Frauen, Männer und Jugendliche, Visagistik, Nageldesign und Wimpernverlängerun an - eine bestimmte Zielgruppe gibt es eigentlich nicht - es sollen alle angesprochen werden.
Aufgabenstellung
Ich hätte gerne einen Flyer, welcher beidseitig bedruckt wird und welchen ich dann per Postwurfsendung an die Haushalte in meiner Umgebung verteilen kann, da ich gerade mein Kosmetikstudio eröffnet habe. Auf der Vorderseite hätte ich gerne meinen Namen, Dipl. Kosmetikerin, Dipl. Make-up-Artist, Dipl. Nageldesignerin, meine Adresse (eventuell kleine Karte) und meine Telefonnummer mit dem Hinweis 'Termine nach telefonischer Vereinbarung' Und meine Mailadresse.
Weiters hätte ich gerne 'Neueröffnung', 'tolle Eröffnungsangbote bis Jahresende', 'kleines Willkommensgeschenk solange der Vorrat reicht' und den Satz 'der erste Eindruck hat keine zweite Chance' darauf. Ansonsten gilt bei der Vorderseite freie Gestaltung!
Auf der Rückseite hätte ich gerne meine Preisliste - ich lade sie mal als PDF-Datei hoch...
Ich lade auch mein Logo, meine Preisliste und ein paar Bilder hoch, die Bilder dürfen verwendet werden, denn ich habe dafür auch bezahlt - ist aber keine Pflicht - bin für jede andere Idee offen! Bevorzugten Farben sind Rosa und Pink, es darf auch versielt sein! Das Format, ob quer, hochgestellt, gefaltet usw. ist mir eigentlich egal - die Preisliste soll nur gut leserlich sein - kann auch von der Anordnung her verändert werden.

```html
<!DOCTYPE html>
<html lang="de">
<head>
<meta charset="utf-8">
<title>Preisliste Kosmetikstudio</title>
<link rel="stylesheet" href="https://fonts.googleapis.com/css2?family=Didact+Gothic&display=swap">
<style>
  :root {
    --magenta: #b1006f;
    --rose: #e0609f;
    --ink: #2b2b2b;
    --paper: #ffffff;
    --skin-light: #f7e6dc;
    --skin-mid: #eccab6;
  }
  * { margin: 0; padding: 0; box-sizing: border-box; }
  html, body { width: 848px; height: 1200px; overflow: hidden; background: var(--paper); }
  .sheet {
    position: relative;
    width: 848px;
    height: 1200px;
    overflow: hidden;
    background: var(--paper);
    font-family: "Didact Gothic", "Century Gothic", sans-serif;
    color: var(--ink);
    font-size: 12.6px;
    line-height: 17.1px;
  }
  .edge {
    position: absolute;
    top: 0;
    width: 17px;
    height: 1200px;
    background: var(--magenta);
    z-index: 3;
  }
  .edge--left { left: 0; }
  .edge--right { right: 0; }
  .portrait {
    position: absolute;
    left: 17px;
    right: 17px;
    bottom: 0;
    height: 300px;
    background:
      radial-gradient(ellipse 70% 60% at 60% 100%, var(--skin-mid) 0%, var(--skin-light) 55%, rgba(255,255,255,0) 100%),
      linear-gradient(to bottom, rgba(255,255,255,0) 0%, var(--skin-light) 100%);
    z-index: 1;
  }
  .column {
    position: absolute;
    top: 23.85px;
    z-index: 2;
  }
  .column--left { left: 36.6px; width: 362.4px; }
  .column--right { left: 449px; width: 362px; }
  .row {
    display: flex;
    justify-content: space-between;
    height: 17.1px;
    white-space: nowrap;
  }
  .row .price { text-align: right; }
  .row--heading { color: var(--rose); }
  .row--group { font-weight: 700; color: var(--ink); }
  .gap { height: 17.1px; }
</style>
</head>
<body>
<div class="sheet">
  <div class="edge edge--left"></div>
  <div class="edge edge--right"></div>
  <div class="portrait" role="img" aria-label="Foto: entspannte Frau liegt mit geschlossenen Augen auf einem weißen Handtuch, eine Hand berührt ihre Stirn"></div>

  <section class="column column--left">
    <div class="row row--heading"><span>Gesichtsbehandlung für Eilige</span></div>
    <div class="row"><span>Reinigung, Hautanalyse, Tonic, Peeling, Maske,</span></div>
    <div class="row"><span>Tagespflege</span><span class="price">25,00 €</span></div>
    <div class="gap"></div>
    <div class="row row--heading"><span>Gesichtsbehandlung klassisch</span></div>
    <div class="row"><span>Reinigung, Hautanalyse, Peeling, Dampf,</span></div>
    <div class="row"><span>Ausreinigen, Tonic, Maske, Lippenpflege,</span></div>
    <div class="row"><span>Massage, Augen- und Tagespflege</span><span class="price">38,00 €</span></div>
    <div class="gap"></div>
    <div class="row row--heading"><span>Gesichtsbehandlung deluxe</span></div>
    <div class="row"><span>Reinigung, Hautanalyse, Peeling, Wimpern oder</span></div>
    <div class="row"><span>Augenbrauen färben, Dampf, Ausreinigen, Tonic,</span></div>
    <div class="row"><span>Augenbrauen faconieren, Ampulle, Maske,</span></div>
    <div class="row"><span>Lippenpflege, Massage, Augen- und Tagespflege</span><span class="price">54,00 €</span></div>
    <div class="gap"></div>
    <div class="row row--heading"><span>Gesichtsbehandlung Anti-Age spezial</span></div>
    <div class="row"><span>Reinigung, Hautanalyse, Peeling, Dampf,</span></div>
    <div class="row"><span>Ausreinigen, Tonic, Ampulle bzw. Serum,</span></div>
    <div class="row"><span>Anti-Aging-Spezialmaske oder Collagen-Vlies</span></div>
    <div class="row"><span>nach Hauttyp, Lippenpflege, Augenampulle,</span></div>
    <div class="row"><span>Massage, Augen- und Antiaging-Tagespflege</span><span class="price">76,00 €</span></div>
    <div class="gap"></div>
    <div class="row row--heading"><span>Microdermabrasionbehandlung</span></div>
    <div class="row"><span>Reinigung, Peeling, Microdermabrasion,</span></div>
    <div class="row"><span>Dampf, Ausreinigen, Ampulle od. Serum,</span></div>
    <div class="row"><span>Maske, Augen- und Tagespflege</span><span class="price">54,00 €</span></div>
    <div class="row"><span>Microdermabrasion-Kur, 4x mit Wochenabstand</span><span class="price">206,00 €</span></div>
    <div class="gap"></div>
    <div class="row row--heading"><span>Fruchtsäurebehandlung</span></div>
    <div class="row"><span>Reinigung, Peeling, AHA-Fruchtsäuretonic,</span></div>
    <div class="row"><span>AHA-Gingkosomengel, Milchsäurevlies,</span></div>
    <div class="row"><span>Massage mit Vit.C-Creme, Augen- und Tagespflege</span><span class="price">64,00 €</span></div>
    <div class="row"><span>Kur, 4x mit Wochenabstand</span><span class="price">245,00 €</span></div>
    <div class="gap"></div>
    <div class="row row--heading"><span>Microdermabrasion mit Fruchtsäure kombiniert</span></div>
    <div class="row"><span>Reinigung, Peeling, Microdermabrasion,</span></div>
    <div class="row"><span>AHA-Fruchtsäuretonic, AHA-Gingkosomengel,</span></div>
    <div class="row"><span>Milchsäure-Vlies, Massage mit Vitamin-C-Creme,</span></div>
    <div class="row"><span>Augen- und Tagespflege</span><span class="price">105,00 €</span></div>
    <div class="row"><span>Kur, 4x mit Wochenabstand</span><span class="price">400,00 €</span></div>
    <div class="gap"></div>
    <div class="row row--heading"><span>Aknespezialbehandlung</span></div>
    <div class="row"><span>Reinigung, Peeling, Dampf, Ausreinigen, Tonic,</span></div>
    <div class="row"><span>Ampulle, Aknespezialmaske, Hochfrequenz,</span></div>
    <div class="row"><span>Spezialtagespflege</span><span class="price">38,00 €</span></div>
    <div class="gap"></div>
    <div class="row row--heading"><span>Pigmentfleckenspezialbehandlung</span></div>
    <div class="row"><span>Reinigung, Peeling, Dampf, Spezialserum,</span></div>
    <div class="row"><span>Spezialmaske gegen Pigmentflecken,</span></div>
    <div class="row"><span>Augenpflege, Spezialtagespflege</span><span class="price">48,00 €</span></div>
    <div class="gap"></div>
    <div class="row row--heading"><span>Anticouperosespezialbehandlung</span></div>
    <div class="row"><span>Reinigung, Peeling, Dampf, Spezialserum,</span></div>
    <div class="row"><span>Spezialmaske, Augenpflege, Spezialtagespflege</span><span class="price">48,00 €</span></div>
    <div class="gap"></div>
    <div class="row"><span>Gesicht-, Hals- und Dekolletémassage (ca. 20 min)</span><span class="price">18,00 €</span></div>
    <div class="row"><span>Kosmetische Lymphdrainage (ca. 30 min)</span><span class="price">23,00 €</span></div>
  </section>

  <section class="column column--right">
    <div class="row row--heading"><span>Zusatzbehandlungen</span></div>
    <div class="row"><span>Wimpern färben</span><span class="price">6,00 €</span></div>
    <div class="row"><span>Augenbrauen färben</span><span class="price">5,00 €</span></div>
    <div class="row"><span>Augenbrauen faconnieren/harzen</span><span class="price">4,00 €</span></div>
    <div class="row"><span>Augen-Intensivbehandlung</span><span class="price">19,00 €</span></div>
    <div class="row"><span>Wimperndauerwelle</span><span class="price">18,00 €</span></div>
    <div class="row"><span>Kinn harzen</span><span class="price">6,00 €</span></div>
    <div class="row"><span>Oberlippe harzen</span><span class="price">4,00 €</span></div>
    <div class="row"><span>Wirkstoffampulle</span><span class="price">10,00 €</span></div>
    <div class="row"><span>Hochfrequenz</span><span class="price">6,00 €</span></div>
    <div class="gap"></div>
    <div class="row"><span class="row--heading">Cellulite-/Entschlackungswickel</span><span class="price">32,00 €</span></div>
    <div class="row"><span>10er-Block: 10+1 gratis</span><span class="price">320,00 €</span></div>
    <div class="gap"></div>
    <div class="row row--heading"><span>Hände</span></div>
    <div class="row"><span>Klassische Maniküre mit Pflege oder Farb-Lack</span><span class="price">16,00 €</span></div>
    <div class="row"><span>Maniküre, mit Handpeeling und Paraffinbad</span><span class="price">32,00 €</span></div>
    <div class="row"><span>Handpeeling + Paraffinbad</span><span class="price">18,00 €</span></div>
    <div class="gap"></div>
    <div class="row"><span>Permanenter Gel-Lack am Naturnagel</span><span class="price">16,00 €</span></div>
    <div class="row"><span>Permanent French-Manicure</span><span class="price">2,00 €</span></div>
    <div class="row"><span>Gel-Lack entfernen, mit Pflege</span><span class="price">12,00 €</span></div>
    <div class="gap"></div>
    <div class="row"><span>Nagelmodellage mit Gel (neues Set)</span><span class="price">54,00 €</span></div>
    <div class="row"><span>Auffüllen „All inclusive“</span></div>
    <div class="row"><span>(French, Fullcover, Glitzer; Nailart/Steinchen/</span></div>
    <div class="row"><span>Airbrush/Sticker auf 2 Fingern)</span><span class="price">38,00 €</span></div>
    <div class="row"><span>Nailart/Steinchen/Airbrush/Sticker zusätzlich pro Finger</span><span class="price">0,50 €</span></div>
    <div class="row"><span>Modellage entfernen mit Pflege</span><span class="price">16,00 €</span></div>
    <div class="gap"></div>
    <div class="row row--heading"><span>Permanente Wimpernverlängerung</span></div>
    <div class="row"><span>Erstes Set</span><span class="price">115,00 €</span></div>
    <div class="row"><span>Auffüllen innerhalb von 3 Wochen</span><span class="price">38,00 €</span></div>
    <div class="row"><span>Innerhalb von 4–5 Wochen</span><span class="price">48,00 €</span></div>
    <div class="gap"></div>
    <div class="row row--heading"><span>Enthaarung</span></div>
    <div class="row"><span>Beine harzen inklusive Knie</span><span class="price">18,00 €</span></div>
    <div class="row"><span>Beine komplett harzen</span><span class="price">28,00 €</span></div>
    <div class="row"><span>Achseln harzen</span><span class="price">11,00 €</span></div>
    <div class="row"><span>Bikinizone harzen</span><span class="price">12,00 €</span></div>
    <div class="row"><span>Arme komplett harzen</span><span class="price">22,00 €</span></div>
    <div class="row"><span>Harz-Package KLEIN</span></div>
    <div class="row"><span>(Beine inklusive Knien, Achseln, Bikinizone)</span><span class="price">38,00 €</span></div>
    <div class="row"><span>Harz-Package GROSS</span></div>
    <div class="row"><span>(Beine, Achseln, Bikinizone, Arme)</span><span class="price">68,00 €</span></div>
    <div class="gap"></div>
    <div class="row row--group"><span>Männer:</span></div>
    <div class="row"><span>Rücken harzen</span><span class="price">26,00 €</span></div>
    <div class="row"><span>Brust und Bauch harzen</span><span class="price">26,00 €</span></div>
    <div class="gap"></div>
    <div class="row row--heading"><span>Make up</span></div>
    <div class="row"><span>Dezentes Tages-Make-Up</span><span class="price">22,00 €</span></div>
    <div class="row"><span>Abend-Make-Up</span><span class="price">28,00 €</span></div>
    <div class="row"><span>Hochzeits-Make-Up inklusive 1 Probetermin</span><span class="price">55,00 €</span></div>
    <div class="row"><span>Braut-Package</span></div>
    <div class="row"><span>(Probe-Make-Up, Make-Up am Tag der Hochzeit,</span></div>
    <div class="row"><span>Nagelmodellage, Wimpernverlängerung)</span><span class="price">205,00 €</span></div>
  </section>
</div>
</body>
</html>
```